Professional, elegant brochure for funeral home

We have a funeral home. We would like a 2 sided brochure. On one side will be 3 columns for our cremation options and on the other side would be 2-3 columns of our burial options. Would like to print it and also will be putting it on our website at www.Veltranoserves.com

Use as examples

https://www.bardwellhaven.com/pricing-and-resources/online-cremation-package-options

https://pellingtonmortuary.com/wp-content/uploads/Cremation-with-Ceremony-Plans.pdf

We only need a simple 1page (front and back brochure). Once we have decided on the designer I can provide the final content to be placed on the brochure.

Target Market(s)

We are family owned business so Something soft, inviting, personable and looks professionally done.

Industry/Entity Type

Funeral Home

Requirements
Must have
• Look professional. Easy to read
Nice to have
• Softer Muted comforting colors. No bright colors.

```html
<!DOCTYPE html>
<html lang="en">
<head>
<meta charset="utf-8">
<title>Rest Easy Plan – Martin L. Veltrano Funeral Home</title>
<link href="https://fonts.googleapis.com/css2?family=Montserrat:wght@400;500;600;700;800&display=swap" rel="stylesheet">
<style>
  :root {
    --backdrop: #2e2e2f;
    --paper: #ffffff;
    --ink: #2a2a2a;
    --header: #232324;
    --lime: #b5d334;
    --lime-deep: #6fb43a;
    --blue: #1f6fb8;
    --blue-deep: #3a3a9c;
    --teal: #1aa3c9;
    --placeholder: #4a4a4c;
    --frame: #d9d9d9;
  }
  * { box-sizing: border-box; margin: 0; padding: 0; }
  html, body { width: 1200px; height: 776px; overflow: hidden; }
  body {
    background: var(--backdrop);
    font-family: "Montserrat", sans-serif;
    color: var(--ink);
    position: relative;
  }
  .sheet {
    position: absolute;
    top: 44px;
    width: 500px;
    height: 690px;
    background: var(--paper);
    overflow: hidden;
    box-shadow: 0 10px 30px rgba(0,0,0,.45);
  }
  .sheet--front { left: 70px; }
  .sheet--back { left: 630px; }

  .masthead { position: absolute; inset: 0 0 auto 0; height: 160px; }
  .masthead svg { position: absolute; inset: 0; }
  .brand {
    position: absolute; left: 28px; top: 40px;
    display: flex; align-items: center; gap: 10px;
    color: #fff; font-weight: 600; line-height: 1.05;
  }
  .brand__dot { width: 30px; height: 30px; border-radius: 50%; background: var(--lime); }
  .brand__name { font-size: 11px; letter-spacing: .5px; }
  .brand__name strong { display: block; font-size: 24px; font-weight: 600; letter-spacing: 1px; }
  .brand__tagline { position: absolute; left: 28px; top: 104px; color: #fff; font-size: 11px; font-weight: 600; }
  .plan-title { position: absolute; right: 24px; top: 42px; width: 210px; text-align: center; }
  .plan-title h1 { color: #fff; font-size: 24px; font-weight: 700; }
  .plan-title p { color: var(--lime); font-size: 10.5px; font-weight: 700; margin-top: 6px; line-height: 1.25; }

  .option-frame {
    position: absolute; top: 182px;
    border: 1.5px solid var(--frame);
    border-radius: 40px;
    padding: 8px;
  }
  .option {
    height: 100%;
    border-radius: 34px;
    padding: 16px 12px;
    color: #fff;
    font-size: 8.5px; line-height: 1.35;
    position: relative;
  }
  .option h2 { font-size: 17px; font-weight: 800; margin-bottom: 6px; display: flex; align-items: center; gap: 8px; }
  .option svg { stroke: #fff; fill: none; stroke-width: 2; }
  .option--info { background: linear-gradient(180deg, var(--lime) 0%, var(--lime-deep) 100%); border-radius: 14px 40px 14px 60px; }
  .option--data { background: linear-gradient(180deg, var(--blue-deep) 0%, var(--blue) 50%, var(--teal) 100%); }
  .option--work { background: linear-gradient(180deg, var(--lime-deep) 0%, var(--lime) 100%); border-radius: 40px 40px 60px 14px; }
  .option__icon { position: absolute; left: 14px; bottom: 20px; }
  .option__icon--top { position: static; margin-bottom: 14px; }

  .front-note {
    position: absolute; left: 40px; right: 40px; top: 572px;
    font-size: 11px; line-height: 1.45; text-align: center;
  }

  .services-head { position: absolute; top: 168px; left: 0; right: 0; text-align: center; }
  .services-head h2 { font-size: 23px; font-weight: 800; letter-spacing: .3px; }
  .services-head p { font-size: 11.5px; font-weight: 700; color: #555; }
  .service { position: absolute; left: 28px; right: 28px; height: 78px; display: flex; align-items: center; gap: 14px; }
  .service--right { flex-direction: row-reverse; text-align: right; }
  .service__photo { flex: none; width: 74px; height: 74px; border-radius: 50%; background: var(--placeholder); }
  .service h3 { font-size: 14px; font-weight: 700; color: #3a3a3a; }
  .service p { font-size: 8.5px; line-height: 1.35; }
</style>
</head>
<body>

<section class="sheet sheet--front">
  <header class="masthead">
    <svg width="500" height="160" viewBox="0 0 500 160" aria-hidden="true">
      <path d="M0 0H500V108C400 130 300 104 200 124C120 140 60 132 0 124Z" fill="var(--header)"/>
      <path d="M0 128C60 136 120 144 200 128C300 108 400 134 500 112" stroke="var(--blue)" stroke-width="4" fill="none"/>
      <path d="M0 134C60 142 120 150 200 134C300 114 400 140 500 118" stroke="var(--lime)" stroke-width="4" fill="none"/>
    </svg>
    <div class="brand"><span class="brand__dot"></span><span class="brand__name">MARTIN L.<strong>VELTRANO</strong>FUNERAL HOME</span></div>
    <div class="brand__tagline">Cremation · Burial · Pre-Planning</div>
    <div class="plan-title"><h1>Rest Easy plan</h1><p>Thinking Ahead can bring lasting peace to your loved ones</p></div>
  </header>

  <div class="option-frame" style="left:26px;width:150px;height:330px">
    <div class="option option--info">
      <h2>INFO
        <svg width="26" height="18" viewBox="0 0 26 18"><path d="M2 6h5l10-5v16L7 12H2z"/><path d="M20 5l4-2M20 9h5M20 13l4 2"/></svg>
      </h2>
      <p>Lorem ipsum dolor sit amet, consectetuer adipiscing elit, sed diam nonummy nibh euismod tincidunt ut laoreet dolore magna aliquam erat volutpat. Ut wisi enim ad minim veniam, quis nostrud exerci tation ullamcorper suscipit lobortis nisl ut aliquip.</p>
      <svg class="option__icon" width="48" height="34" viewBox="0 0 48 34"><path d="M2 11h10l20-9v30L12 23H2z"/><path d="M38 9l7-4M38 17h9M38 25l7 4"/></svg>
    </div>
  </div>

  <div class="option-frame" style="left:180px;width:140px;height:330px;border-radius:50px">
    <div class="option option--data" style="border-radius:44px">
      <svg class="option__icon--top" width="50" height="52" viewBox="0 0 50 52"><rect x="4" y="2" width="42" height="48" rx="3"/><path d="M12 12h26M12 22h26M28 40h10"/></svg>
      <h2>
        <svg width="22" height="24" viewBox="0 0 22 24"><rect x="2" y="2" width="18" height="20" rx="2"/><path d="M6 8h10M6 13h10"/></svg>DATA
      </h2>
      <p>Lorem ipsum dolor sit amet, consectetuer adipiscing elit, sed diam nonummy nibh euismod tincidunt ut laoreet dolore magna aliquam erat volutpat. Ut wisi enim ad minim veniam, quis nostrud exerci tation ullamcorper suscipit lobortis nisl ut aliquip.</p>
    </div>
  </div>

  <div class="option-frame" style="left:326px;width:148px;height:330px">
    <div class="option option--work">
      <h2>WORK
        <svg width="20" height="24" viewBox="0 0 20 24"><path d="M10 2c5 4 5 12 3 16H7C5 14 5 6 10 2z"/><path d="M7 18l-3 4M13 18l3 4"/></svg>
      </h2>
      <p>Lorem ipsum dolor sit amet, consectetuer adipiscing elit, sed diam nonummy nibh euismod tincidunt ut laoreet dolore magna aliquam erat volutpat. Ut wisi enim ad minim veniam, quis nostrud exerci tation ullamcorper suscipit lobortis nisl.</p>
      <svg class="option__icon" width="50" height="50" viewBox="0 0 50 50"><path d="M42 8C30 8 20 18 16 30l4 4c12-4 22-14 22-26z"/><circle cx="32" cy="18" r="4"/><path d="M16 30l-8 2 4-10M20 34l-2 8 10-4M6 44l6-6"/></svg>
    </div>
  </div>

  <p class="front-note">Lorem ipsum dolor sit amet, consectetuer adipiscing elit, sed diam nonummy nibh euismod tincidunt ut laoreet dolore magna aliquam erat volutpat. Ut wisi enim ad minim veniam, quis nostrud exerci tation ullamcorper suscipit lobortis nisl ut aliquip ex ea commodo consequat. Duis autem vel eum iriure dolor in hendrerit in vulputate velit esse molestie consequat, vel illum dolore eu feugiat nulla facilisis at vero eros</p>
</section>

<section class="sheet sheet--back">
  <header class="masthead">
    <svg width="500" height="160" viewBox="0 0 500 160" aria-hidden="true">
      <path d="M0 0H500V108C400 130 300 104 200 124C120 140 60 132 0 124Z" fill="var(--header)"/>
      <path d="M0 128C60 136 120 144 200 128C300 108 400 134 500 112" stroke="var(--blue)" stroke-width="4" fill="none"/>
      <path d="M0 134C60 142 120 150 200 134C300 114 400 140 500 118" stroke="var(--lime)" stroke-width="4" fill="none"/>
    </svg>
    <div class="brand"><span class="brand__dot"></span><span class="brand__name">MARTIN L.<strong>VELTRANO</strong>FUNERAL HOME</span></div>
    <div class="brand__tagline">Cremation · Burial · Pre-Planning</div>
    <div class="plan-title"><h1>Rest Easy plan</h1><p>Thinking Ahead can bring lasting peace to your loved ones</p></div>
  </header>

  <div class="services-head">
    <h2>OUR SIGNATURE SERVICES</h2>
    <p>Options to consider as you plan the ceremony</p>
  </div>

  <article class="service" style="top:236px"><div class="service__photo" role="img" aria-label="Service photo"></div><div><h3>Your Heading</h3><p>Lorem ipsum dolor sit amet, consectetuer adipiscing elit, sed diam nonummy nibh euismod tincidunt ut laoreet dolore magna aliquam erat volutpat. Ut wisi enim ad minim veniam, quis nostrud exerci tation ullamcorper suscipit lobortis nisl ut aliquip ex ea commodo consequat.</p></div></article>
  <article class="service service--right" style="top:316px"><div class="service__photo" role="img" aria-label="Service photo"></div><div><h3>Your Heading</h3><p>Lorem ipsum dolor sit amet, consectetuer adipiscing elit, sed diam nonummy nibh euismod tincidunt ut laoreet dolore magna aliquam erat volutpat. Ut wisi enim ad minim veniam, quis nostrud exerci tation ullamcorper suscipit lobortis nisl ut aliquip ex ea commodo consequat.</p></div></article>
  <article class="service" style="top:396px"><div class="service__photo" role="img" aria-label="Service photo"></div><div><h3>Your Heading</h3><p>Lorem ipsum dolor sit amet, consectetuer adipiscing elit, sed diam nonummy nibh euismod tincidunt ut laoreet dolore magna aliquam erat volutpat. Ut wisi enim ad minim veniam, quis nostrud exerci tation ullamcorper suscipit lobortis nisl ut aliquip ex ea commodo consequat.</p></div></article>
  <article class="service service--right" style="top:476px"><div class="service__photo" role="img" aria-label="Service photo"></div><div><h3>Your Heading</h3><p>Lorem ipsum dolor sit amet, consectetuer adipiscing elit, sed diam nonummy nibh euismod tincidunt ut laoreet dolore magna aliquam erat volutpat. Ut wisi enim ad minim veniam, quis nostrud exerci tation ullamcorper suscipit lobortis nisl ut aliquip ex ea commodo consequat.</p></div></article>
  <article class="service" style="top:556px"><div class="service__photo" role="img" aria-label="Service photo"></div><div><h3>Your Heading</h3><p>Lorem ipsum dolor sit amet, consectetuer adipiscing elit, sed diam nonummy nibh euismod tincidunt ut laoreet dolore magna aliquam erat volutpat. Ut wisi enim ad minim veniam, quis nostrud exerci tation ullamcorper suscipit lobortis nisl ut aliquip ex ea commodo consequat.</p></div></article>
</section>

</body>
</html>
```